Crest of Morning Paddocks Business Cards with logo

Need a creative business card that pops. Colorful but professional. The attached logo should be included. We are a national horse racing partnership so we are in the equine business. Nothing cartoonlike or whimsical.

Target Market(s)

professionals - 40+

Contact Information for Business Card

Maren Dunleavy
Director of Operations
27 Ashbrook Lane
Middletown, MD. 21584

Phone (313) 555-0147

FX: (949) 555-0192

email: maren@cmpaddocks.example
cmpaddocks.example

Requirements
Must have
• All information above should be on the business card including the website address. Professional yet creative
Nice to have
• an attention grabbing design. not boring. exciting.
Should not have
• cartoon like - whimsical.

```html
<!DOCTYPE html>
<html lang="en">
<head>
<meta charset="utf-8">
<title>Crest of Morning Paddocks – Business Card</title>
<link href="https://fonts.googleapis.com/css2?family=Arimo:wght@400;700&display=swap" rel="stylesheet">
<style>
  :root {
    --stage: #e9ebef;
    --navy: #272b62;
    --navy-deep: #1c1f4c;
    --gold: #b8923a;
    --gold-light: #c9a44d;
    --white: #ffffff;
    --muted: #c5c8de;
    --accent: #e9b9a8;
  }
  * { box-sizing: border-box; margin: 0; padding: 0; }
  html, body {
    width: 1200px; height: 900px; overflow: hidden;
    background: var(--stage);
    font-family: "Arimo", Arial, sans-serif;
  }
  .card {
    position: absolute; left: 150px; top: 193px;
    width: 900px; height: 514px; overflow: hidden;
    background: linear-gradient(100deg, var(--navy) 0%, var(--navy-deep) 60%, var(--navy) 100%);
    box-shadow: 0 14px 40px rgba(20, 22, 50, .25);
  }
  .gold-band {
    position: absolute; left: 661px; top: 0; width: 239px; height: 100%;
    background: linear-gradient(180deg, var(--gold-light), var(--gold));
  }
  .brand-mark-small {
    position: absolute; left: 36px; top: 28px; width: 150px;
    display: flex; align-items: center; gap: 10px;
  }
  .brand-mark-small .dot {
    flex: none; width: 22px; height: 22px; border-radius: 50%;
    background: var(--gold);
  }
  .brand-mark-small .name {
    color: var(--white); font-weight: 700; font-size: 15px;
    line-height: 1.25; text-transform: uppercase; letter-spacing: 1px;
  }
  .person { position: absolute; left: 34px; top: 184px; }
  .person .full-name { color: var(--white); font-weight: 700; font-size: 31px; }
  .person .role { color: var(--muted); font-size: 16px; margin-top: 6px; }
  .address {
    position: absolute; left: 38px; top: 296px;
    color: var(--muted); font-size: 16px; line-height: 24px;
  }
  .contact {
    position: absolute; left: 34px; top: 402px;
    list-style: none; font-size: 17px; line-height: 26px;
  }
  .contact li { display: flex; align-items: center; gap: 12px; color: var(--accent); }
  .contact li.web { color: var(--muted); }
  .contact svg { width: 18px; height: 18px; fill: var(--muted); flex: none; }
  .brand-disc {
    position: absolute; left: 451px; top: 50px; width: 420px; height: 420px;
    border-radius: 50%; background: var(--white);
    display: flex; align-items: center; justify-content: center; text-align: center;
  }
  .brand-disc .name {
    color: var(--navy); font-weight: 700; font-size: 40px; line-height: 1.2;
    text-transform: uppercase; letter-spacing: 4px; width: 300px;
  }
</style>
</head>
<body>
  <div class="card">
    <div class="gold-band"></div>

    <div class="brand-mark-small">
      <span class="dot"></span>
      <span class="name">Crest of Morning Paddocks</span>
    </div>

    <div class="person">
      <div class="full-name">Maren Dunleavy</div>
      <div class="role">Director of Operations</div>
    </div>

    <div class="address">
      27 Ashbrook Lane<br>
      Middletown, MD. 21584
    </div>

    <ul class="contact">
      <li><svg viewBox="0 0 24 24"><path d="M6.6 10.8a15 15 0 0 0 6.6 6.6l2.2-2.2a1 1 0 0 1 1-.25 11.4 11.4 0 0 0 3.6.57 1 1 0 0 1 1 1V20a1 1 0 0 1-1 1A17 17 0 0 1 3 4a1 1 0 0 1 1-1h3.5a1 1 0 0 1 1 1c0 1.25.2 2.45.57 3.6a1 1 0 0 1-.25 1z"/></svg>(313) 555-0147</li>
      <li><svg viewBox="0 0 24 24"><path d="M6 3h9l3 3v4H6zM4 11h16a2 2 0 0 1 2 2v6H2v-6a2 2 0 0 1 2-2zm2 4v4h12v-4z"/></svg>(949) 555-0192</li>
      <li class="web"><svg viewBox="0 0 24 24"><path d="M3 5h18v14H3zm2 2v.5l7 5 7-5V7z"/></svg>maren@cmpaddocks.example</li>
      <li class="web"><svg viewBox="0 0 24 24"><path d="M12 2a10 10 0 1 0 0 20 10 10 0 0 0 0-20zm0 2c.9 1.2 1.7 3 2 5h-4c.3-2 1.1-3.8 2-5zM4.3 11h3.7a16 16 0 0 0 0 2H4.3a8 8 0 0 1 0-2zm5.7 0h4a14 14 0 0 1 0 2h-4a14 14 0 0 1 0-2zm6 0h3.7a8 8 0 0 1 0 2H16a16 16 0 0 0 0-2zm-6 4h4c-.3 2-1.1 3.8-2 5-.9-1.2-1.7-3-2-5z"/></svg>cmpaddocks.example</li>
    </ul>

    <div class="brand-disc">
      <span class="name">Crest of Morning Paddocks</span>
    </div>
  </div>
</body>
</html>
```